Maplecrest Counseling and Consulting, LLC

We need a business card and stationary designed for a new therapy practice for Laura Whitcombe. Laura Whitcombe is a Therapist who specializes in Therapy for children dealing with trauma and/or stress. Below are some of her thoughts:
colors can include purple, blue, turquoise and green (does NOT have to be all colors) See attached Logos
Laura Whitcombe, LMHC
Maplecrest Counseling & Counseling Inc.
4382 W. Harbor Parkway
Suite 714
Boca Raton, FL 33912
Phone: 561-730-2254
Fax: 561-730-2255
Email: laura@maplecrestcc-example.com
Website: www.maplecrestcc-example.com

```html
<!DOCTYPE html>
<html lang="en">
<head>
<meta charset="utf-8">
<title>Maplecrest Counseling – Business Card</title>
<link rel="stylesheet" href="https://fonts.googleapis.com/css2?family=Lato:wght@400;700&display=swap">
<style>
  :root {
    --page-bg: #e4e4e4;
    --card-bg: #ffffff;
    --brand-green: #7cb342;
    --band-grey: #6d6e70;
    --ink: #2b2b2b;
    --muted: #7a7a7a;
    --on-band: #ffffff;
  }
  * { box-sizing: border-box; margin: 0; padding: 0; }
  html, body {
    width: 1200px; height: 926px; overflow: hidden;
    background: var(--page-bg);
    font-family: "Lato", Arial, sans-serif;
  }
  .business-card {
    position: absolute; left: 100px; top: 177px;
    width: 1000px; height: 572px;
    background: var(--card-bg);
    box-shadow: 0 10px 30px rgba(0,0,0,.18);
    overflow: hidden;
  }
  .card-curves { position: absolute; inset: 0; width: 1000px; height: 572px; }
  .brand {
    position: absolute; left: 70px; top: 120px;
    display: flex; align-items: center; gap: 12px;
  }
  .brand-dot { width: 22px; height: 22px; border-radius: 50%; background: var(--band-grey); }
  .brand-name { font-size: 21px; font-weight: 400; color: var(--ink); }
  .contact-list {
    position: absolute; left: 70px; top: 236px;
    list-style: none; font-size: 21px; color: var(--ink);
  }
  .contact-list li { display: flex; align-items: center; gap: 14px; height: 32px; }
  .contact-icon { width: 20px; height: 20px; fill: var(--brand-green); }
  .person { position: absolute; right: 70px; top: 190px; text-align: right; }
  .person-name { font-size: 42px; color: var(--brand-green); font-weight: 400; letter-spacing: .5px; }
  .person-name strong { font-weight: 700; }
  .person-credential { font-size: 19px; color: var(--muted); margin-top: -2px; }
  .practice { font-size: 20px; font-weight: 700; color: var(--brand-green); margin-top: 16px; }
  .address { font-size: 21px; color: var(--ink); line-height: 1.45; margin-top: 6px; font-style: normal; }
  .website {
    position: absolute; right: 70px; bottom: 34px;
    font-size: 26px; color: var(--on-band); letter-spacing: .5px;
  }
</style>
</head>
<body>
  <article class="business-card">
    <svg class="card-curves" viewBox="0 0 1000 572" aria-hidden="true">
      <path d="M0 405 C 250 395, 600 400, 1000 455 L1000 572 L0 572 Z" fill="var(--band-grey)"/>
      <path d="M0 378 C 180 385, 420 400, 620 418 C 420 408, 200 402, 0 400 Z" fill="var(--brand-green)"/>
      <path d="M0 400 C 200 402, 420 408, 620 418 C 400 410, 200 408, 0 410 Z" fill="#ffffff"/>
    </svg>

    <div class="brand">
      <span class="brand-dot"></span>
      <span class="brand-name">Maplecrest Counseling and Consulting, Inc.</span>
    </div>

    <ul class="contact-list">
      <li>
        <svg class="contact-icon" viewBox="0 0 20 20" aria-label="Phone"><path d="M2 6c0-2 3-3 8-3s8 1 8 3v2h-4V6.5H6V8H2z M4 9h12l2 8H2z"/></svg>
        561-730-2254
      </li>
      <li>
        <svg class="contact-icon" viewBox="0 0 20 20" aria-label="Fax"><path d="M5 2h10v5H5z M2 8h16v7h-3v3H5v-3H2z M7 13v3h6v-3z" fill-rule="evenodd"/></svg>
        561-730-2255
      </li>
      <li>
        <svg class="contact-icon" viewBox="0 0 20 20" aria-label="Email"><path d="M1 4h18v12H1z"/><path d="M2 5l8 6 8-6" stroke="#fff" stroke-width="1.6" fill="none"/></svg>
        laura@maplecrestcc-example.com
      </li>
    </ul>

    <div class="person">
      <h1 class="person-name">Laura <strong>Whitcombe</strong></h1>
      <div class="person-credential">- LMHC</div>
      <div class="practice">Maplecrest Counseling &amp; Counseling Inc.</div>
      <address class="address">
        4382 W. Harbor Parkway<br>
        Suite 714<br>
        Boca Raton, FL 33912
      </address>
    </div>

    <div class="website">www.maplecrestcc-example.com</div>
  </article>
</body>
</html>
```